Social Search engine to end child poverty

Velquor.org is a search engine based in Houston, that donates 50% or more of its profits to nonprofit organizations that focus on ending child poverty. We consider itself a social business, claims to support full financial transparency,protect the privacy of its users;

Velquor shows advertisements next to its search results, and is paid by partners every time a user is directed to an advertiser via a sponsored link.
We are committed to becoming a privacy friendly search engine. Searches will be encrypted, not stored permanently, and data will not not sold to third party advertisers.
Like www.parvink.org Every search done by website visitor will generate a TUPRAK that will be stored in his wallet. Then the visitor can donate these TUPRAKS to The idea behind is evry donation will put a SMILE back on a child face

The search engine will partner with foundations/associations/NGOs that will be able to propose crowdfunding campaigns on the landing page

The beta test will be done with african children. So the landing page should show faces of happiness, joy, children

Please find attached inspirational ideas in the PDF file

Target Market(s)

NGO, Foundation, association, donators based in USA

Industry/Entity Type

Charity

Number of Pages Required

5+ page

Colors
33a6d7
fbed22
f04a50
a54499
f78d1f
add136

Requirements
Must have
• Landing page
• 0- Number of TUPRAKS collected worlwide/number of projects funded
• 1- explaining how it works and
• 2- samples of fundable projects
• 3- Become partner
• Search results
• 1- Sponsored results should be differentiated
• 2- The search page should advertise initiative pr people that acts in the world to end child poverty.
• 3 It should also provide quizzes with some metrics/figures on child poverty
• Under the search engine bar should be "News" "Videos

```html
<!DOCTYPE html>
<html lang="en">
<head>
<meta charset="utf-8">
<title>Velquor.org — Give Meaning To Your Searches</title>
<link href="https://fonts.googleapis.com/css2?family=IBM+Plex+Sans:wght@400;500;600;700&display=swap" rel="stylesheet">
<style>
  :root {
    --navy-deep: #15233b;
    --navy: #1d2e4b;
    --navy-soft: #2a3d5c;
    --red: #f04a50;
    --white: #ffffff;
    --white-dim: rgba(255, 255, 255, 0.82);
  }
  * { margin: 0; padding: 0; box-sizing: border-box; }
  html, body { width: 1200px; height: 784px; overflow: hidden; }
  body {
    font-family: "IBM Plex Sans", Arial, sans-serif;
    color: var(--white);
    background: var(--navy-deep);
  }
  .hero {
    position: relative;
    width: 1200px;
    height: 784px;
    overflow: hidden;
  }
  .hero-photo {
    position: absolute;
    inset: 0;
    background:
      radial-gradient(ellipse at 45% 40%, var(--navy-soft) 0%, transparent 60%),
      radial-gradient(ellipse at 80% 65%, #3a3550 0%, transparent 45%),
      linear-gradient(180deg, var(--navy-deep) 0%, var(--navy) 55%, #2c3b55 100%);
  }
  .site-header {
    position: absolute;
    top: 0; left: 0; right: 0;
    height: 124px;
  }
  .brand {
    position: absolute;
    left: 144px;
    top: 38px;
    font-size: 38px;
    font-weight: 700;
    letter-spacing: -0.5px;
    line-height: 48px;
    color: var(--white);
  }
  .donate-button {
    position: absolute;
    left: 895px;
    top: 45px;
    width: 108px;
    height: 38px;
    border-radius: 19px;
    background: var(--red);
    color: var(--white);
    font-size: 14.5px;
    font-weight: 600;
    text-align: center;
    line-height: 38px;
    letter-spacing: 0.3px;
  }
  .menu-icon {
    position: absolute;
    left: 1023px;
    top: 50px;
    width: 33px;
    height: 28px;
  }
  .menu-icon span {
    position: absolute;
    left: 0;
    width: 33px;
    height: 5px;
    border-radius: 1px;
    background: var(--white);
  }
  .menu-icon span:nth-child(1) { top: 0; }
  .menu-icon span:nth-child(2) { top: 11.5px; }
  .menu-icon span:nth-child(3) { top: 23px; }

  .headline {
    position: absolute;
    top: 188px;
    left: 0; right: 0;
    text-align: center;
    font-size: 48px;
    font-weight: 700;
    line-height: 60px;
  }
  .tagline {
    position: absolute;
    top: 270px;
    left: 0; right: 0;
    text-align: center;
    font-size: 23px;
    font-weight: 500;
    line-height: 32px;
  }

  .stats {
    position: absolute;
    top: 380px;
    left: 0; right: 0;
  }
  .stat {
    position: absolute;
    top: 0;
    width: 170px;
    text-align: center;
  }
  .stat-ring {
    position: absolute;
    left: 15px;
    top: 0;
    width: 140px;
    height: 140px;
  }
  .stat-icon {
    position: absolute;
    left: 66px;
    top: 27px;
    width: 38px;
    height: 38px;
  }
  .stat-value {
    position: absolute;
    left: 0; right: 0;
    top: 72px;
    font-size: 29px;
    font-weight: 700;
    line-height: 38px;
    letter-spacing: 0.5px;
  }
  .stat-label {
    position: absolute;
    left: -10px; right: -10px;
    top: 154px;
    font-size: 17px;
    font-weight: 500;
    line-height: 25px;
  }

  .search-form {
    position: absolute;
    left: 330px;
    top: 622px;
    width: 540px;
    height: 44px;
    display: flex;
    border-radius: 22px;
    background: var(--white);
    overflow: hidden;
  }
  .search-field {
    flex: 1;
    padding-left: 22px;
    font-size: 15px;
    line-height: 44px;
    color: #7a8597;
  }
  .search-button {
    width: 110px;
    background: var(--red);
    color: var(--white);
    font-size: 14.5px;
    font-weight: 600;
    letter-spacing: 0.3px;
    text-align: center;
    line-height: 44px;
  }
  .tuprak-note {
    position: absolute;
    top: 676px;
    left: 0; right: 0;
    text-align: center;
    font-size: 14px;
    font-weight: 400;
    color: var(--white-dim);
  }
  .copyright {
    position: absolute;
    top: 718px;
    left: 0; right: 0;
    text-align: center;
    font-size: 16px;
    font-weight: 500;
  }
</style>
</head>
<body>
<main class="hero">
  <div class="hero-photo" role="img" aria-label="Photo of two smiling children sitting together outdoors, under a dark navy overlay"></div>

  <header class="site-header">
    <div class="brand">Velquor.org</div>
    <a class="donate-button">DONATE</a>
    <div class="menu-icon" aria-label="Menu"><span></span><span></span><span></span></div>
  </header>

  <h1 class="headline">Give Meaning To Your Searches</h1>
  <p class="tagline">With Velquor, your searches funds programs targeting<br>disadvantaged children</p>

  <section class="stats">
    <div class="stat" style="left:192px">
      <svg class="stat-ring" viewBox="0 0 140 140">
        <circle cx="70" cy="70" r="67" fill="none" stroke="#ffffff" stroke-width="3.5"/>
        <circle cx="70" cy="70" r="67" fill="none" stroke="#f04a50" stroke-width="3.5" stroke-dasharray="339 82" transform="rotate(90 70 70)"/>
      </svg>
      <svg class="stat-icon" viewBox="0 0 38 38" fill="none" stroke="#ffffff" stroke-width="3" stroke-linecap="round">
        <circle cx="19" cy="19" r="17"/>
        <circle cx="13" cy="15" r="1.2" fill="#ffffff"/>
        <circle cx="25" cy="15" r="1.2" fill="#ffffff"/>
        <path d="M11.5 22.5 Q19 29.5 26.5 22.5"/>
      </svg>
      <div class="stat-value">2031</div>
      <p class="stat-label">TUPRAKS collected<br>worldwide</p>
    </div>

    <div class="stat" style="left:405px">
      <svg class="stat-ring" viewBox="0 0 140 140">
        <circle cx="70" cy="70" r="67" fill="none" stroke="#ffffff" stroke-width="3.5"/>
        <circle cx="70" cy="70" r="67" fill="none" stroke="#f04a50" stroke-width="3.5" stroke-dasharray="339 82" transform="rotate(90 70 70)"/>
      </svg>
      <svg class="stat-icon" viewBox="0 0 38 38" fill="none" stroke="#ffffff" stroke-width="3" stroke-linecap="round">
        <circle cx="19" cy="19" r="17"/>
        <circle cx="13" cy="15" r="1.2" fill="#ffffff"/>
        <circle cx="25" cy="15" r="1.2" fill="#ffffff"/>
        <path d="M11.5 22.5 Q19 29.5 26.5 22.5"/>
      </svg>
      <div class="stat-value">230</div>
      <p class="stat-label">Projects<br>funded</p>
    </div>

    <div class="stat" style="left:618px">
      <svg class="stat-ring" viewBox="0 0 140 140">
        <circle cx="70" cy="70" r="67" fill="none" stroke="#ffffff" stroke-width="3.5"/>
        <circle cx="70" cy="70" r="67" fill="none" stroke="#f04a50" stroke-width="3.5" stroke-dasharray="339 82" transform="rotate(90 70 70)"/>
      </svg>
      <svg class="stat-icon" viewBox="0 0 38 38" fill="none" stroke="#ffffff" stroke-width="3" stroke-linecap="round">
        <circle cx="19" cy="19" r="17"/>
        <circle cx="13" cy="15" r="1.2" fill="#ffffff"/>
        <circle cx="25" cy="15" r="1.2" fill="#ffffff"/>
        <path d="M11.5 22.5 Q19 29.5 26.5 22.5"/>
      </svg>
      <div class="stat-value">54133</div>
      <p class="stat-label">Searches<br>made this month</p>
    </div>

    <div class="stat" style="left:832px">
      <svg class="stat-ring" viewBox="0 0 140 140">
        <circle cx="70" cy="70" r="67" fill="none" stroke="#ffffff" stroke-width="3.5"/>
        <circle cx="70" cy="70" r="67" fill="none" stroke="#f04a50" stroke-width="3.5" stroke-dasharray="339 82" transform="rotate(90 70 70)"/>
      </svg>
      <svg class="stat-icon" viewBox="0 0 38 38" fill="none" stroke="#ffffff" stroke-width="3" stroke-linecap="round">
        <circle cx="19" cy="19" r="17"/>
        <circle cx="13" cy="15" r="1.2" fill="#ffffff"/>
        <circle cx="25" cy="15" r="1.2" fill="#ffffff"/>
        <path d="M11.5 22.5 Q19 29.5 26.5 22.5"/>
      </svg>
      <div class="stat-value">2031</div>
      <p class="stat-label">Smiles put back<br>on children's faces</p>
    </div>
  </section>

  <form class="search-form" role="search">
    <div class="search-field">Search the web and earn TUPRAKS…</div>
    <div class="search-button">SEARCH</div>
  </form>
  <p class="tuprak-note">Every search earns a TUPRAK for your wallet — donate it to a project and put a smile back on a child's face.</p>

  <footer class="copyright">© Copyright 2020 Velquor.org. All Rights Reserved.</footer>
</main>
</body>
</html>
```